Дизайн сайта рекламного агентства
Название компании, продукта или адрес сайта
"Медиа-Ладья" (MD-Ladya)
Для агентства интернет-рекламы "Медиа-Ладья" (MD-Ladya) нужен дизайн сайта. Домен: md-ladya.ru. Агентство оказывает услуги по настройке и ведению контекстной рекламы, рекламы в соц сетях, медийной рекламы.
Требования к дизайну:
- уникальность
- оригинальность
- креативность
- современность
- простота
- удобство
Сайт должен вызывать у посетителя доверие, позитивные эмоции, а самое главное – вызвать желание сотрудничества.
Логотип прикрепляется в двух вариантах цветовой гаммы.
Тип сайта
Сайт-визитка
Укажите ссылки на сайты, которые нравятся
brightcrew-demo.ru
pomeranz-demo.ru
www.kvelt-demo.ru
zt07-demo.ru
Логотип для светлого фона сайта
Текстура, которую можно использовать в дизайне, но ТОЛЬКО как дополнительный вариант!
Логотип для темного фона сайта
Комментарии и пожелания для дизайнеров
В самом видимом месте будет располагаться слоган (его не придумали, идеи приветствуются), который будет мотивировать посетителей на сотрудничество, например, "Вы узнали о нас? Мы сделаем так, чтобы узнали о вас тоже!". Рядом несколько ключевых преимуществ агентства. Под логотипом нужно поместить надпись "Агентство интернет-рекламы". Также на сайте будет меню (компания, услуги, цены, контакты), телефон сверху и снизу, кнопки соц сетей, контентная часть В будущем будут и такие пункты, как "сертификаты", "партнеры", "отзывы", но т.к. на начальном этапе функционирования агентства их не будет, то для них пока нужно лишь предусмотреть место.

```html
<!DOCTYPE html>
<html lang="ru">
<head>
<meta charset="utf-8">
<title>MD-Ladya — агентство интернет-рекламы</title>
<link rel="stylesheet" href="https://fonts.googleapis.com/css2?family=Open+Sans:wght@300;400;600;700&display=swap">
<style>
  :root {
    --red: #d42a3c;
    --ink: #ffffff;
    --night: #1f2b37;
    --footer-bg: #111419;
    --muted: #4f6477;
    --link-red: #e0435a;
    --phone-grey: #8e9aa8;
    --panel: rgba(40, 12, 14, 0.62);
  }
  * { box-sizing: border-box; margin: 0; padding: 0; }
  html, body { width: 1187px; height: 1200px; overflow: hidden; background: var(--night); }
  body { font-family: "Open Sans", Arial, sans-serif; color: var(--ink); }
  .page { position: relative; width: 1187px; height: 1200px; overflow: hidden; background: var(--night); }

  .hero-bg {
    position: absolute; left: 0; top: 0; width: 1187px; height: 656px;
    background:
      radial-gradient(ellipse 480px 360px at 880px 230px, rgba(232, 92, 70, 0.85), transparent 70%),
      radial-gradient(ellipse 520px 380px at 520px 360px, rgba(200, 60, 62, 0.7), transparent 72%),
      radial-gradient(ellipse 400px 400px at 60px 480px, rgba(40, 30, 70, 0.9), transparent 75%),
      linear-gradient(180deg, #3a1a24 0%, #7c2a33 45%, #5a2030 80%, #3b2035 100%);
  }

  /* Header */
  .site-header {
    position: absolute; left: 0; top: 0; width: 100%; height: 75px;
    background: rgba(18, 18, 24, 0.82);
  }
  .brand { position: absolute; display: flex; align-items: center; gap: 6px; }
  .brand-dot { width: 34px; height: 34px; border-radius: 50%; background: var(--red); }
  .brand-name { font-size: 24px; font-weight: 700; color: var(--ink); letter-spacing: -0.5px; white-space: nowrap; }
  .site-header .brand { left: 151px; top: 21px; }
  .main-nav { position: absolute; left: 404px; top: 29px; display: flex; gap: 26px; }
  .main-nav a { color: var(--ink); font-size: 13px; text-decoration: underline; white-space: nowrap; }
  .contact-box { position: absolute; right: 151px; text-align: right; }
  .site-header .contact-box { top: 14px; }
  .phone { font-size: 22px; font-weight: 300; color: var(--ink); line-height: 1.1; white-space: nowrap; }
  .phone .code { color: var(--phone-grey); }
  .callback { display: inline-block; font-size: 11px; color: var(--phone-grey); text-decoration: underline; margin-top: 3px; }

  /* Slogan */
  .slogan-title {
    position: absolute; left: 168px; top: 147px; width: 359px; height: 54px;
    background: var(--red); font-size: 31px; font-weight: 700; line-height: 54px;
    padding-left: 12px; letter-spacing: 0.3px; white-space: nowrap;
  }
  .slogan-sub {
    position: absolute; left: 235px; top: 191px; width: 292px; height: 31px;
    background: var(--red); font-size: 12px; font-weight: 600; text-align: right;
    padding: 3px 12px 0 0; line-height: 16px; white-space: nowrap;
  }
  .about-links { position: absolute; right: 661px; top: 238px; text-align: right; }
  .about-links a { display: block; color: var(--ink); font-size: 13px; text-decoration: underline; white-space: nowrap; }
  .about-links .link-company { margin-bottom: 12px; }
  .about-links .link-active {
    position: relative; text-decoration: none; background: var(--red);
    height: 31px; line-height: 31px; padding: 0 14px 0 10px;
    margin: 0 -14px 12px auto; width: max-content; text-align: left;
  }
  .about-links .link-active::after {
    content: ""; position: absolute; right: -10px; top: 0;
    border-left: 10px solid var(--red); border-top: 15.5px solid transparent; border-bottom: 15.5px solid transparent;
  }

  .intro-panel {
    position: absolute; left: 565px; top: 146px; width: 471px; height: 263px;
    background: var(--panel); border-radius: 8px; padding: 14px 18px 14px 20px;
  }
  .intro-panel h2 { font-size: 16px; font-weight: 600; margin-bottom: 13px; }
  .intro-panel p { font-size: 10.2px; line-height: 16.5px; letter-spacing: -0.1px; }
  .intro-panel p + p { margin-top: 16px; }

  /* Portfolio */
  .portfolio {
    position: absolute; left: 151px; top: 434px; width: 885px; height: 443px;
    display: grid; grid-template-columns: repeat(4, 1fr); grid-template-rows: repeat(2, 1fr);
    box-shadow: 0 14px 16px -8px rgba(0, 0, 0, 0.55);
  }
  .tile { width: 100%; height: 100%; }
  .tile-resort { background: linear-gradient(180deg, #8fb6d8 0%, #4d7f6a 45%, #26b7d8 75%, #3a6b3a 100%); }
  .tile-truck { background: linear-gradient(180deg, #8aa1b4 0%, #c9d6de 45%, #6b7a88 75%, #9aa9b8 100%); }
  .tile-dress { background: radial-gradient(ellipse at 55% 45%, #6d6f78 0%, #2c2f3a 60%, #1d2029 100%); }
  .tile-apple { background: radial-gradient(ellipse at 55% 50%, #e8cfc0 0%, #f2f2ee 60%, #a8c860 100%); }
  .tile-city { background: linear-gradient(180deg, #0d2a4a 0%, #1e5c90 45%, #4fb0e6 65%, #0b2440 100%); }
  .tile-portrait { background: radial-gradient(ellipse at 45% 45%, #c98a5a 0%, #8a4a24 55%, #e8c890 100%); }
  .tile-bedroom { background: linear-gradient(180deg, #d8d0c4 0%, #e8e2d8 45%, #8a6c54 80%, #5a3a24 100%); }
  .tile-deli { background: radial-gradient(ellipse at 50% 50%, #b8443a 0%, #8a2a24 50%, #c87c52 100%); }

  .portfolio-banner {
    position: absolute; left: 297px; top: 449px; width: 594px; height: 46px;
    background: var(--red); font-size: 25px; font-weight: 700; text-align: center; line-height: 46px; white-space: nowrap;
  }

  /* Advantages */
  .advantages { position: absolute; left: 151px; top: 934px; width: 885px; display: flex; gap: 46px; }
  .advantage { width: 264px; }
  .advantage h3 { font-size: 12px; font-weight: 400; color: var(--link-red); text-decoration: underline; margin-bottom: 14px; white-space: nowrap; }
  .advantage p { font-size: 10.5px; line-height: 15px; color: var(--muted); }

  /* Footer */
  .site-footer { position: absolute; left: 0; top: 1102px; width: 100%; height: 98px; background: var(--footer-bg); }
  .site-footer .brand { left: 151px; top: 31px; }
  .copyright { position: absolute; left: 333px; top: 32px; font-size: 11px; line-height: 18px; color: #5a6370; white-space: nowrap; }
  .social { position: absolute; left: 526px; top: 35px; display: flex; gap: 5px; }
  .social span { width: 19px; height: 19px; border-radius: 50%; border: 1px solid #2c333c; background: #181c22; }
  .site-footer .contact-box { top: 23px; }
</style>
</head>
<body>
<div class="page">
  <div class="hero-bg" role="img" aria-label="Красная гранжевая текстура с царапинами"></div>

  <header class="site-header">
    <div class="brand"><span class="brand-dot"></span><span class="brand-name">MD-Ladya</span></div>
    <nav class="main-nav">
      <a href="#">Главная</a><a href="#">Компания</a><a href="#">Услуги</a><a href="#">Цены</a><a href="#">Контакты</a>
    </nav>
    <div class="contact-box">
      <div class="phone"><span class="code">+7 (495)</span> 000-48-26</div>
      <a class="callback" href="#">Заказать звонок</a>
    </div>
  </header>

  <h1 class="slogan-title">ВЫ УЗНАЛИ О НАС?</h1>
  <div class="slogan-sub">Мы сделаем так, чтобы узнали о вас тоже!</div>

  <nav class="about-links">
    <a class="link-company" href="#">О компании</a>
    <a class="link-active" href="#">Чем мы занимаемся</a>
    <a href="#">Почему стоит выбрать нас</a>
  </nav>

  <section class="intro-panel">
    <h2>Давайте знакомиться!</h2>
    <p>Мы – команда молодых и крайне амбициозных профессионалов с пятилетним опытом работы и портфолио для более чем 100 клиентов.<br>"MD Ladya" – агентство небольших размеров и огромных возможностей. Находясь в Топ-20 российских агентств по обороту и количеству клиентов, мы постоянно двигаемся вперед, поднимая планку своих достижений каждый день!</p>
    <p>Нам есть чем выделиться среди коллег. Во-первых, все наши идеи максимально креативны и направлены на удовлетворение потребностей конкретного клиента. Во-вторых, в нашем арсенале имеется ряд технологических решений, которых Вы не найдете больше нигде. Уникальные технологии - результат нашего опыта в конкретных направлениях цифрового маркетинга.</p>
  </section>

  <section class="portfolio">
    <div class="tile tile-resort" role="img" aria-label="Курорт с бассейном и небоскрёбами"></div>
    <div class="tile tile-truck" role="img" aria-label="Грузовик на заснеженной дороге"></div>
    <div class="tile tile-dress" role="img" aria-label="Модель в тёмном платье"></div>
    <div class="tile tile-apple" role="img" aria-label="Девушка с зелёными яблоками"></div>
    <div class="tile tile-city" role="img" aria-label="Ночной город у воды"></div>
    <div class="tile tile-portrait" role="img" aria-label="Портрет девушки в тёплом свете"></div>
    <div class="tile tile-bedroom" role="img" aria-label="Интерьер спальни с люстрой"></div>
    <div class="tile tile-deli" role="img" aria-label="Мясные деликатесы и колбасы"></div>
  </section>
  <div class="portfolio-banner">БОЛЕЕ 200 РЕАЛИЗОВАННЫХ ПРОЕКТОВ</div>

  <section class="advantages">
    <div class="advantage">
      <h3>Постоплатная система работы</h3>
      <p>Вы платите только за выполненный результат работы. Это наша отличительная черта, мы уверены в качестве и результате своей работы, поэтому всегда работаем по постоплатной схеме.</p>
    </div>
    <div class="advantage">
      <h3>Готовый продукт на каждом этапе работы</h3>
      <p>Любой этап нашей работы заканчивается созданием готового продукта, который вы уже можете использовать. Это значит, что вы платите только за то, что действительно приносит вполне конкретную выгоду для вас.</p>
    </div>
    <div class="advantage">
      <h3>Конкретные цифры и статистика</h3>
      <p>На первых этапах проекта мы всегда совместно с вами разрабатываем прозрачные и понятные системы измерения эффективности нашей работы. Больше никаких непонятных терминов и оправданий.</p>
    </div>
  </section>

  <footer class="site-footer">
    <div class="brand"><span class="brand-dot"></span><span class="brand-name">MD-Ladya</span></div>
    <div class="copyright">© 1997–2013<br>Рекламное агентство «MD Ladya»</div>
    <div class="social" aria-label="Социальные сети"><span></span><span></span><span></span><span></span><span></span></div>
    <div class="contact-box">
      <div class="phone"><span class="code">+7 (495)</span> 000-48-26</div>
      <a class="callback" href="#">Заказать звонок</a>
    </div>
  </footer>
</div>
</body>
</html>
```